Stylish new business card needed!

Hello everyone! I am in need of a new business card design for an alarm company here in Hurricane WV. I have all fonts, color codes and logos provided for you use! We are a young company and like the style of a clean sleek looking business card. Would like it double sided, one side holding the logo and the other with your design!
Target Market(s)
The people that are looking for the newest tech for home automation and security
Industry/Entity Type
Alarm services; Home automation
Contact Information for Business Card
Name of person; position (Sales; Installer); Phone Number (555.419.7362); Employee cell Number; Website (www.GuardedByVelm.example); Employee Email; Double sided
Look and feel
Each slider illustrates characteristics of the customer's brand and the style your logo design should communicate.

```html
<!DOCTYPE html>
<html lang="en">
<head>
<meta charset="utf-8">
<title>Velm Business Card</title>
<link rel="stylesheet" href="https://fonts.googleapis.com/css2?family=Roboto:wght@300;400;700&display=swap">
<style>
  :root {
    --page-bg: #f1f1f1;
    --card-orange: #f4914f;
    --card-grey: #9b9b9b;
    --ink-white: #ffffff;
    --ink-black: #111111;
    --accent: #f4914f;
  }
  * { box-sizing: border-box; margin: 0; padding: 0; }
  html, body {
    width: 1200px;
    height: 1200px;
    overflow: hidden;
    background: var(--page-bg);
    font-family: "Roboto", Arial, sans-serif;
  }
  .canvas {
    position: relative;
    width: 1200px;
    height: 1200px;
  }
  .card {
    position: absolute;
    left: 177px;
    width: 846px;
    height: 498px;
    overflow: hidden;
  }
  .card--front { top: 87px; background: var(--card-orange); color: var(--ink-white); }
  .card--back { top: 615px; background: var(--card-grey); }

  .holder {
    position: absolute;
    left: 56px;
    top: 102px;
  }
  .holder__name {
    font-weight: 300;
    font-size: 27px;
    line-height: 31px;
    text-transform: uppercase;
    letter-spacing: 0.3px;
  }
  .holder__role {
    font-weight: 300;
    font-size: 23px;
    line-height: 30px;
    margin-top: 2px;
  }

  .contacts {
    position: absolute;
    left: 56px;
    top: 296px;
    list-style: none;
  }
  .contacts__item {
    display: flex;
    align-items: center;
    height: 33px;
    font-weight: 300;
    font-size: 21px;
  }
  .contacts__item--web { font-weight: 700; }
  .contacts__item--address { margin-top: 17px; }
  .contacts__icon {
    width: 28px;
    height: 28px;
    margin-right: 15px;
    flex: none;
  }

  .wordmark {
    position: absolute;
    font-weight: 400;
    line-height: 1;
    letter-spacing: 4px;
  }
  .wordmark--front {
    left: 455px;
    top: 170px;
    font-size: 132px;
    color: var(--ink-white);
  }
  .wordmark--back {
    left: 0;
    right: 0;
    top: 150px;
    text-align: center;
    font-size: 210px;
    color: var(--ink-black);
  }
</style>
</head>
<body>
<main class="canvas">

  <section class="card card--front" aria-label="Card front">
    <div class="holder">
      <p class="holder__name">Marcus<br>Hollenbeck</p>
      <p class="holder__role">CEO, President</p>
    </div>

    <ul class="contacts">
      <li class="contacts__item">
        <svg class="contacts__icon" viewBox="0 0 28 28" aria-hidden="true">
          <circle cx="14" cy="14" r="14" fill="#fff"/>
          <path d="M9.5 7.5l2.6-.4 1.4 3.4-1.6 1.2a8 8 0 0 0 3.8 3.8l1.2-1.6 3.4 1.4-.4 2.6c-5.5.6-11-4.9-10.4-10.4z" fill="var(--accent)"/>
        </svg>
        555.419.7362
      </li>
      <li class="contacts__item">
        <svg class="contacts__icon" viewBox="0 0 28 28" aria-hidden="true">
          <circle cx="14" cy="14" r="14" fill="#fff"/>
          <rect x="7" y="9" width="14" height="10" fill="none" stroke="var(--accent)" stroke-width="1.6"/>
          <path d="M7 9l7 6 7-6" fill="none" stroke="var(--accent)" stroke-width="1.6"/>
        </svg>
        info@velm.example
      </li>
      <li class="contacts__item contacts__item--web">
        <svg class="contacts__icon" viewBox="0 0 28 28" aria-hidden="true">
          <circle cx="14" cy="14" r="14" fill="#fff"/>
          <circle cx="14" cy="14" r="7.5" fill="none" stroke="var(--accent)" stroke-width="1.6"/>
          <ellipse cx="14" cy="14" rx="3.2" ry="7.5" fill="none" stroke="var(--accent)" stroke-width="1.4"/>
          <path d="M6.5 14h15" stroke="var(--accent)" stroke-width="1.4"/>
        </svg>
        www.GuardedByVelm.example
      </li>
      <li class="contacts__item contacts__item--address">
        <svg class="contacts__icon" viewBox="0 0 28 28" aria-hidden="true">
          <circle cx="14" cy="14" r="14" fill="#fff"/>
          <path d="M14 21s-5.5-5.6-5.5-9.2a5.5 5.5 0 0 1 11 0C19.5 15.4 14 21 14 21z" fill="var(--accent)"/>
          <circle cx="14" cy="11.8" r="2" fill="#fff"/>
        </svg>
        48 Ridgeline Ave Milton WV 25541
      </li>
    </ul>

    <p class="wordmark wordmark--front">VELM</p>
  </section>

  <section class="card card--back" aria-label="Card back">
    <p class="wordmark wordmark--back">VELM</p>
  </section>

</main>
</body>
</html>
```